Zielgruppe
Wir sind eine Wäscherei.
Zielgruppe: Kunden aus der Hotel- und Gastronomiebranche
Aufgabenstellung
Wir benötigen einen 2-seitigen Flyer DIN lang. 9,8 x21cm
TextInhalte sind in der Vorlage-Datei.
Bilder sind eingefügt.

```html
<!DOCTYPE html>
<html lang="de">
<head>
<meta charset="utf-8">
<title>Wäscherei Talbrunn – Flyer DIN lang</title>
<link href="https://fonts.googleapis.com/css2?family=Jost:wght@400;500;600;700&display=swap" rel="stylesheet">
<style>
  :root {
    --magenta: #c2127f;
    --ink: #1a1a1a;
    --paper: #ffffff;
    --stage: #f1f1f1;
  }
  * { box-sizing: border-box; margin: 0; padding: 0; }
  html, body { width: 1200px; height: 1200px; overflow: hidden; }
  body {
    background: var(--stage);
    font-family: "Jost", "Futura", sans-serif;
    color: var(--ink);
    position: relative;
  }
  .flyer-side {
    position: absolute;
    left: 100px;
    width: 1000px;
    height: 467px;
    background: var(--paper);
    overflow: hidden;
  }
  .flyer-side--front { top: 95px; }
  .flyer-side--back { top: 638px; }
  .photo-layer { position: absolute; inset: 0; width: 1000px; height: 467px; }

  /* front */
  .brand-name {
    position: absolute; left: 48px; top: 118px;
    font-size: 34px; font-weight: 700; letter-spacing: 0.5px;
    color: var(--magenta); text-transform: uppercase;
  }
  .service-title {
    position: absolute; left: 48px; top: 212px;
    font-size: 15.5px; font-weight: 600; color: var(--magenta);
  }
  .service-list {
    position: absolute; left: 48px; top: 234px;
    list-style: none; font-size: 15.5px; line-height: 20.2px;
  }
  .service-list li::before {
    content: ""; display: inline-block; width: 4px; height: 4px;
    background: var(--magenta); margin: 0 5px 3px 0; transform: rotate(45deg);
  }
  .contact-line {
    position: absolute; left: 48px; bottom: 45px;
    font-size: 10px; display: flex; align-items: center; gap: 5px;
  }
  .contact-line .dot { width: 3px; height: 3px; background: var(--magenta); transform: rotate(45deg); }
  .contact-line svg { width: 10px; height: 10px; }

  /* back */
  .offer-heading {
    position: absolute; left: 48px; top: 52px;
    border-left: 3px solid var(--magenta); padding-left: 8px;
    color: var(--magenta); line-height: 1.1;
  }
  .offer-heading strong { display: block; font-size: 19px; font-weight: 700; text-transform: uppercase; }
  .offer-heading span { font-size: 18px; font-weight: 400; }
  .offer-intro {
    position: absolute; left: 64px; top: 112px;
    font-size: 15px; line-height: 19.5px; width: 560px;
  }
  .price-group { position: absolute; top: 200px; font-size: 15px; line-height: 19.5px; }
  .price-group--one { left: 64px; top: 222px; }
  .price-group--two { left: 330px; }
  .price-group b { font-weight: 700; }
  .offer-extra { position: absolute; left: 64px; top: 292px; font-size: 15px; line-height: 19.5px; }
  .vat-note { position: absolute; left: 64px; top: 356px; font-size: 9px; }
  .back-footer {
    position: absolute; left: 64px; bottom: 30px;
    display: flex; align-items: center; gap: 6px; font-size: 9.5px;
  }
  .back-footer .footer-brand { color: var(--magenta); font-weight: 700; font-size: 10px; text-transform: uppercase; }
  .back-footer .dot { width: 3px; height: 3px; background: var(--magenta); transform: rotate(45deg); }
  .back-footer svg { width: 9px; height: 9px; }
</style>
</head>
<body>

<section class="flyer-side flyer-side--front">
  <svg class="photo-layer" viewBox="0 0 1000 467" aria-hidden="false">
    <defs>
      <linearGradient id="banquetTones" x1="0" y1="0" x2="1" y2="1">
        <stop offset="0" stop-color="#e6dfdc"/>
        <stop offset="0.5" stop-color="#f2eef1"/>
        <stop offset="1" stop-color="#d9d3da"/>
      </linearGradient>
    </defs>
    <circle cx="845" cy="230" r="292" fill="var(--magenta)"/>
    <circle cx="858" cy="230" r="284" fill="url(#banquetTones)" role="img" aria-label="Foto: festlich gedeckte Bankett-Tafel mit Gläsern, weißen Servietten und Blumengesteck"/>
  </svg>

  <div class="brand-name">Wäscherei Talbrunn</div>
  <div class="service-title">Serviettenfaltservice – ab November 2017</div>
  <ul class="service-list">
    <li>Hotel- und Gastronomiewäsche</li>
    <li>Schmutzmatten</li>
    <li>Gardinenservice</li>
    <li>Berufskleidung</li>
    <li>Private Wäsche</li>
    <li>Verkauf von Hotel- und Gastronomietextilien</li>
  </ul>
  <div class="contact-line">
    <span>Wäscherei Falkner</span><i class="dot"></i>
    <span>Lindenweg 14</span><i class="dot"></i>
    <span>72814 Hainstadt</span>
    <svg viewBox="0 0 10 10"><path d="M2 1 L4 3 L3 4.5 Q4.5 6.5 5.5 7 L7 6 L9 8 L7.5 9.5 Q3 8.5 0.5 2.5 Z" fill="var(--magenta)"/></svg>
    <span>+49 (0) 7000 / 12 34 56</span>
    <svg viewBox="0 0 10 10"><rect x="0.5" y="2" width="9" height="6.5" fill="none" stroke="var(--magenta)"/><path d="M0.5 2 L5 6 L9.5 2" fill="none" stroke="var(--magenta)"/></svg>
    <span>info@waescherei-falkner.de</span>
  </div>
</section>

<section class="flyer-side flyer-side--back">
  <svg class="photo-layer" viewBox="0 0 1000 467">
    <defs>
      <linearGradient id="tableTones" x1="0" y1="0" x2="1" y2="1">
        <stop offset="0" stop-color="#9aa6b2"/>
        <stop offset="0.5" stop-color="#e8e6e4"/>
        <stop offset="1" stop-color="#c9b28a"/>
      </linearGradient>
      <linearGradient id="napkinTones" x1="0" y1="0" x2="1" y2="1">
        <stop offset="0" stop-color="#6a4a6e"/>
        <stop offset="0.5" stop-color="#ece8ee"/>
        <stop offset="1" stop-color="#d6cfd8"/>
      </linearGradient>
    </defs>
    <circle cx="895" cy="110" r="152" fill="var(--magenta)"/>
    <circle cx="905" cy="110" r="146" fill="url(#tableTones)" role="img" aria-label="Foto: gedeckter Restauranttisch mit Weingläsern und gefalteter Serviette"/>
    <circle cx="945" cy="330" r="140" fill="var(--magenta)"/>
    <circle cx="953" cy="326" r="134" fill="url(#napkinTones)" role="img" aria-label="Foto: Tischgedeck mit zur Bischofsmütze gefalteten Stoffservietten und Gläsern"/>
  </svg>

  <h2 class="offer-heading"><strong>Ihr Serviettenfaltservice</strong><span>ab November 2017</span></h2>
  <p class="offer-intro">
    Wir optimieren Ihren Serviettenfaltprozess.<br>
    Wir entlasten Sie von dieser demotivierenden und unproduktiven Tätigkeit.<br>
    Wir falten Ihnen Ihre Stoffservietten oder unsere Mietservietten vor.<br>
    Hygienisch, zuverlässig und wirtschaftlich – bereit für die Mise en Place.
  </p>
  <div class="price-group price-group--one">
    Faltformen – Kategorie 1:<br><b>Welle, Kerze, Fächer</b><br>je Faltung für nur 0,20 € *
  </div>
  <div class="price-group price-group--two" style="top:222px">
    Faltformen – Kategorie 2:<br><b>Pyramide, Bischofsmütze</b><br>je Faltung für nur 0,35 € *
  </div>
  <p class="offer-extra">
    Weitere Formen sind auf Anfrage möglich.<br>
    Bei Bedarf stellen wir Ihnen Mietservietten für nur 0,25 €* je Stück zur Verfügung.<br>
    Mindestabnahmemenge: 100 Stück
  </p>
  <p class="vat-note">*zzgl. gesetzliche MwSt.</p>
  <div class="back-footer">
    <span class="footer-brand">Wäscherei Talbrunn</span>
    <span>Kontakt: Wäscherei Falkner</span><i class="dot"></i>
    <span>Lindenweg 14</span><i class="dot"></i>
    <span>72814 Hainstadt</span>
    <svg viewBox="0 0 10 10"><path d="M2 1 L4 3 L3 4.5 Q4.5 6.5 5.5 7 L7 6 L9 8 L7.5 9.5 Q3 8.5 0.5 2.5 Z" fill="var(--magenta)"/></svg>
    <span>+49 (0) 7000 / 12 34 56</span>
    <svg viewBox="0 0 10 10"><rect x="0.5" y="2" width="9" height="6.5" fill="none" stroke="var(--magenta)"/><path d="M0.5 2 L5 6 L9.5 2" fill="none" stroke="var(--magenta)"/></svg>
    <span>info@waescherei-falkner.de</span>
  </div>
</section>

</body>
</html>
```